Melissa Dorvan Personal Business Card

I like orange. It's would better if my card have an orange background
Address: 5820 Halvers Lane #417
San Jose
California
US
Tel: 4085172049

Industry/Entity Type

Business

```html
<!DOCTYPE html>
<html lang="en">
<head>
<meta charset="utf-8">
<title>Melissa Dorvan — Business Card</title>
<link rel="stylesheet" href="https://fonts.googleapis.com/css2?family=Monsieur+La+Doulaise&family=Saira+Condensed:wght@400&display=swap">
<style>
  :root {
    --magenta: #dd1279;
    --orange: #e57718;
    --ink: #3b2a20;
    --white: #ffffff;
  }
  html, body {
    margin: 0;
    padding: 0;
    width: 1200px;
    height: 684px;
    overflow: hidden;
    background: var(--magenta);
  }
  .card {
    position: relative;
    width: 1200px;
    height: 684px;
    background: var(--magenta);
    overflow: hidden;
  }
  .card__blob {
    position: absolute;
    inset: 0;
    width: 1200px;
    height: 684px;
    display: block;
  }
  .card__blob path {
    fill: var(--orange);
  }
  .card__name {
    position: absolute;
    left: 0;
    top: 168px;
    width: 1200px;
    margin: 0;
    text-align: center;
    font-family: "Monsieur La Doulaise", cursive;
    font-weight: 400;
    font-size: 118px;
    line-height: 1;
    color: var(--white);
    white-space: nowrap;
  }
  .card__contact {
    position: absolute;
    left: 0;
    top: 609px;
    width: 1200px;
    margin: 0;
    text-align: center;
    font-family: "Saira Condensed", sans-serif;
    font-weight: 400;
    font-size: 34px;
    line-height: 1.2;
    color: var(--ink);
    white-space: nowrap;
  }
</style>
</head>
<body>
  <main class="card">
    <svg class="card__blob" viewBox="0 0 1051 600" preserveAspectRatio="none" aria-hidden="true">
      <path d="M0,390 C120,220 300,40 480,0 L740,0 C800,0 842,60 836,140 C830,230 805,290 775,332 C900,332 1000,385 1051,455 L1051,600 L0,600 Z"/>
    </svg>
    <h1 class="card__name">Melissa Dorvan</h1>
    <p class="card__contact">5820 Halvers Lane #417, San Jose, California U.S.A. Tel: 4085172049</p>
  </main>
</body>
</html>
```